Trovane KLD Omnia Suction Cooker Ad Campaign

We need a full color, full page ad designed for print & digital publishing, showing the versatility of our Trovane KLD Omnia Suction Cooker.

The ad should show the diversity of size ranges, that allow everyone from a Chef to Food Production Facility to use our mixers

The ad should also show the diversity of products, from mayonnaise to ketchup, sauces to dressings, & soups to smoothies

The ad should explain that you can mix, blend, homogenize, emulsify, puree, & liquefy, under vacuum, as well as cook & chill in one unit.

It is a true "All In One" unit that increases production while decreasing labor, extending shelf life while decreasing waste. It also increases batch quality & QA/SQF, HACCP, & GMP standards

I am including the brochure we have, as well as some competitors ads. I am also including a previous ad we had made for an older version. The older version is just an example. Use you imagination, we want to capture the audience

website is www.trovanequip.example

Target Market(s)

Food manufacturers to artisan type chefs that make their own soups, sauces, mayonnaise, ketchup, smoothies & dressings

Requirements
Must have
• Trovane logo
Trovane website
Equipment picture
Show the diversity of the unit
Nice to have
• Use of your imagination to communicate the diversity of the machine, from food production to chefs.
Should not have
• Be professional and unique. Use you imagination to capture energy and communicate to the customer and grab their attention.

NO STAIL, LACK OF ENERGY DESIGNS

```html
<!DOCTYPE html>
<html lang="en">
<head>
<meta charset="utf-8">
<title>Trovane KLD Omnia Suction Cooker – Print Ad</title>
<link rel="stylesheet" href="https://fonts.googleapis.com/css2?family=Montserrat:wght@600;700;800;900&family=Open+Sans:wght@400;600;700&display=swap">
<style>
  :root{
    --bg:#e4e4e2;
    --white:#ffffff;
    --ink:#1d1d1f;
    --charcoal:#2a2c30;
    --charcoal-hi:#4a4d53;
    --red:#d3202a;
    --red-deep:#a5141c;
    --blue:#1f5fae;
    --blue-deep:#163f7a;
    --steel-hi:#e9ecef;
    --steel-lo:#8d949c;
    --muted:#5b5f66;
  }
  *{box-sizing:border-box;margin:0;padding:0}
  html,body{width:741px;height:1200px;overflow:hidden;background:var(--bg)}
  body{font-family:"Open Sans",Arial,sans-serif;color:var(--ink);position:relative}

  .ad{position:absolute;left:20px;top:104px;width:701px;height:991px;background:var(--white);overflow:hidden;box-shadow:0 2px 10px rgba(0,0,0,.18)}

  /* header */
  .ad-header{position:absolute;left:0;top:0;width:100%;height:96px;background:var(--white);border-bottom:4px solid var(--red)}
  .brand{position:absolute;left:30px;top:26px;display:flex;align-items:center;gap:10px}
  .brand-dot{width:26px;height:26px;border-radius:50%;background:var(--red)}
  .brand-name{font-family:"Montserrat",Arial,sans-serif;font-weight:800;font-size:38px;color:var(--red);letter-spacing:-.5px;line-height:1}
  .contact{position:absolute;right:28px;top:20px;font-size:10px;line-height:1.5;color:var(--muted);display:grid;grid-template-columns:auto auto;column-gap:22px}
  .contact strong{color:var(--blue);font-weight:700}

  /* hero */
  .hero{position:absolute;left:0;top:96px;width:100%;height:424px;background:linear-gradient(135deg,var(--charcoal-hi) 0%,var(--charcoal) 55%,#17181a 100%)}
  .hero-title{position:absolute;left:30px;top:30px;width:300px;font-family:"Montserrat",Arial,sans-serif;font-weight:900;font-size:31px;line-height:1.1;color:var(--white)}
  .hero-title .accent{color:var(--red)}
  .hero-copy{position:absolute;left:30px;top:150px;width:290px;color:#d9dbde;font-size:11.5px;line-height:1.55}
  .hero-copy p+p{margin-top:10px}
  .hero-machine{position:absolute;left:340px;top:22px;width:340px;height:380px;border-radius:6px;background:radial-gradient(ellipse at 45% 40%,var(--steel-hi) 0%,#b9bfc6 45%,var(--steel-lo) 100%)}

  /* lower section */
  .lower{position:absolute;left:0;top:520px;width:100%;height:471px}
  .lower svg{position:absolute;left:0;top:0}
  .how-title{position:absolute;left:30px;top:22px;font-family:"Montserrat",Arial,sans-serif;font-weight:800;font-size:26px;color:var(--white)}
  .step{position:absolute;left:28px;width:330px;display:flex;align-items:center;gap:16px}
  .step-photo{flex:0 0 86px;height:86px;border-radius:50%;border:4px solid var(--red);background:radial-gradient(circle at 40% 40%,#d7dbdf 0%,#9aa1a9 60%,#5c6269 100%)}
  .step-text{font-size:11px;line-height:1.5;color:var(--ink)}
  .step-1{top:108px}.step-2{top:210px}.step-3{top:312px}

  .option-photo{position:absolute;border-radius:5px;background:radial-gradient(ellipse at 45% 40%,var(--steel-hi) 0%,#b3bac2 55%,#7d858e 100%);border:3px solid var(--white)}
  .option-photo.a{left:392px;top:86px;width:138px;height:150px}
  .option-photo.b{left:544px;top:66px;width:138px;height:170px}
  .sizes{position:absolute;left:394px;top:246px;width:290px;font-size:11px;color:var(--white);font-weight:600}
  .options{position:absolute;left:394px;top:280px;width:290px;color:var(--white)}
  .options h3{font-family:"Montserrat",Arial,sans-serif;font-size:12.5px;font-weight:700;margin-bottom:8px;color:#ffd34d}
  .options ul{list-style:none;font-size:11px;line-height:1.75}
  .options li{display:flex;align-items:center;gap:8px}
  .options li svg{position:static;flex:0 0 12px}

  .ad-footer{position:absolute;left:0;bottom:0;width:100%;height:14px;background:var(--red)}
</style>
</head>
<body>
<article class="ad">
  <header class="ad-header">
    <div class="brand">
      <span class="brand-dot"></span>
      <span class="brand-name">Trovane</span>
    </div>
    <div class="contact">
      <span><strong>Trovane Mixers, Ltd.</strong></span><span><strong>Tel:</strong> +1 (555) 014-2290</span>
      <span>48 Harbor Row, Suite 3</span><span><strong>Fax:</strong> +1 (555) 014-2291</span>
      <span>Eastwick, ON 20451</span><span>sales@trovanequip.example</span>
      <span></span><span><strong>www.trovanequip.example</strong></span>
    </div>
  </header>

  <section class="hero">
    <h1 class="hero-title"><span class="accent">Trovane</span> KLD Omnia Suction Cooker</h1>
    <div class="hero-copy">
      <p>The Trovane KLD Omnia mixes, blends, homogenizes, emulsifies, purees and liquefies under vacuum, then cooks and chills in a single sealed vessel.</p>
      <p>From small kitchen batches to full production runs, one unit handles mayonnaise, ketchup, sauces, dressings, soups and smoothies with consistent quality.</p>
      <p>Raise output, cut labor, extend shelf life and reduce waste while meeting QA/SQF, HACCP and GMP standards.</p>
    </div>
    <div class="hero-machine" role="img" aria-label="Stainless steel vacuum processor on a tilting frame with control panel"></div>
  </section>

  <section class="lower">
    <svg width="701" height="471" viewBox="0 0 701 471" aria-hidden="true">
      <path d="M0 0 H440 C400 50 300 82 0 92 Z" fill="var(--red)"/>
      <path d="M0 92 C300 82 400 50 440 0 H452 C410 58 310 94 0 102 Z" fill="var(--red-deep)"/>
      <path d="M372 471 V150 C392 90 520 40 701 20 V471 Z" fill="var(--blue)"/>
      <path d="M372 150 C392 90 520 40 701 20 V30 C525 50 400 98 382 160 Z" fill="var(--blue-deep)"/>
    </svg>
    <h2 class="how-title">How It Works:</h2>

    <div class="step step-1">
      <div class="step-photo" role="img" aria-label="Ingredients loaded into the mixing bowl"></div>
      <p class="step-text">Ingredients load into the jacketed bowl and are drawn under vacuum to remove air.</p>
    </div>
    <div class="step step-2">
      <div class="step-photo" role="img" aria-label="High-shear rotor inside the vessel"></div>
      <p class="step-text">The high-shear rotor homogenizes and emulsifies while side scrapers keep walls clean.</p>
    </div>
    <div class="step step-3">
      <div class="step-photo" role="img" aria-label="Finished batch discharging from the valve"></div>
      <p class="step-text">Heat or chill the batch in place, then discharge through the bottom valve.</p>
    </div>

    <div class="option-photo a" role="img" aria-label="Compact bench-size processor for chefs"></div>
    <div class="option-photo b" role="img" aria-label="Production-size processor on stand"></div>
    <p class="sizes">Sizes from 5 to 3,000 liters for chefs and plants alike.</p>
    <div class="options">
      <h3>The following optional features are available:</h3>
      <ul>
        <li><svg width="12" height="12" viewBox="0 0 12 12"><path d="M1 6.5 L4.5 10 L11 2" fill="none" stroke="#ffffff" stroke-width="2"/></svg>Heating &amp; cooling jacket</li>
        <li><svg width="12" height="12" viewBox="0 0 12 12"><path d="M1 6.5 L4.5 10 L11 2" fill="none" stroke="#ffffff" stroke-width="2"/></svg>Variable speed drive</li>
        <li><svg width="12" height="12" viewBox="0 0 12 12"><path d="M1 6.5 L4.5 10 L11 2" fill="none" stroke="#ffffff" stroke-width="2"/></svg>CIP spray system</li>
        <li><svg width="12" height="12" viewBox="0 0 12 12"><path d="M1 6.5 L4.5 10 L11 2" fill="none" stroke="#ffffff" stroke-width="2"/></svg>Tilting discharge frame</li>
        <li><svg width="12" height="12" viewBox="0 0 12 12"><path d="M1 6.5 L4.5 10 L11 2" fill="none" stroke="#ffffff" stroke-width="2"/></svg>Recipe control panel</li>
        <li><svg width="12" height="12" viewBox="0 0 12 12"><path d="M1 6.5 L4.5 10 L11 2" fill="none" stroke="#ffffff" stroke-width="2"/></svg>Load cells &amp; scale</li>
      </ul>
    </div>
  </section>

  <footer class="ad-footer"></footer>
</article>
</body>
</html>
```